4' x 20' Residential Contractor Banner

Design Details

Having 4ftW x 20ft W banners printed that will be placed on our construction dumpsters.

Large Logo & company name!

Background Color:
A bold, medium-dark color like charcoal gray or blacks to ensure banner durability while maintaining a clean, professional look in the elements.
Primary Text Layout:

Services:

Basements:
Highlighted in larger, artistic font with a creative touch (e.g., modern script or bold sans-serif with a shadow or glow effect).
Kitchens & Bathrooms:
Use slightly smaller, complementary fonts below "Basements."

Contact Details:

Phone Number: Prominently displayed in bold, easy-to-read font, font displayed can be (612) 740-9268 or 612.740.9268
Website: Clearly visible, prefer it is not placed below the phone number: www.tallowbrookhomes.com.

Social Media: Include the Facebook link with the Facebook icon: facebook.com/tallowbrookhomesmn.
QR Code if possible:

Add a QR code leading to your website or portfolio. Place it near the contact details with a caption like “Scan for More Info!”
Visual Elements:

Subtle design elements like blueprint-style lines, creative icons, or faint textures to add depth without overwhelming.
Branding:

Consistent color accents from branding (e.g., red, black, gray or white).
Size Considerations:
Ensure all text is legible from a distance. Use high-contrast colors (e.g., white or vibrant accents) against the darker background.
Updates

Designs look the same

Low design quality

Designs look the same

Target Market(s)

Residential Signage

Industry/Entity Type

Construction Remodeling

Font styles to use
Sans Serif

Colors
EB3D1F
EC4F4E
F09395
F8D3D4
FCEDEE

Requirements
Must have
• Extra large company logo visibility.
Nice to have
• QR code, social media icons
Should not have
• To much whites

```html
<!DOCTYPE html>
<html lang="en">
<head>
<meta charset="utf-8">
<title>Tallowbrook Homes – Dumpster Banner</title>
<link href="https://fonts.googleapis.com/css2?family=Arimo:wght@400;700&display=swap" rel="stylesheet">
<style>
  :root {
    --page: #b3b3b3;
    --charcoal: #3a3a3c;
    --red: #e1201f;
    --white: #ffffff;
    --ink: #2a2a2a;
  }
  html, body {
    margin: 0;
    width: 1200px;
    height: 1200px;
    overflow: hidden;
    background: var(--page);
    font-family: "Arimo", Arial, sans-serif;
  }
  .banner {
    position: absolute;
    left: 80px;
    top: 496px;
    width: 1040px;
    height: 207px;
    overflow: hidden;
  }
  .banner-art {
    position: absolute;
    inset: 0;
  }
  .headline {
    position: absolute;
    left: 68px;
    top: 26px;
    margin: 0;
    font-size: 77px;
    font-weight: 400;
    line-height: 1;
    color: var(--red);
    letter-spacing: -0.5px;
  }
  .services {
    position: absolute;
    left: 68px;
    top: 110px;
    margin: 0;
    font-size: 27px;
    font-weight: 400;
    color: var(--white);
  }
  .phone-strip {
    position: absolute;
    left: 0;
    top: 155px;
    width: 248px;
    height: 33px;
    background: var(--white);
  }
  .phone {
    position: absolute;
    left: 66px;
    top: 158px;
    font-size: 25px;
    line-height: 27px;
    color: var(--red);
  }
  .website {
    position: absolute;
    left: 256px;
    top: 158px;
    font-size: 25px;
    line-height: 27px;
    color: var(--white);
  }
  .brand {
    position: absolute;
    left: 566px;
    top: 38px;
    width: 132px;
    height: 132px;
    display: flex;
    flex-direction: column;
    align-items: center;
    justify-content: center;
    gap: 6px;
  }
  .brand-mark {
    width: 22px;
    height: 22px;
    background: var(--red);
  }
  .brand-name {
    font-size: 13px;
    font-weight: 700;
    letter-spacing: 1px;
    color: var(--ink);
    text-align: center;
    line-height: 1.15;
  }
</style>
</head>
<body>
  <div class="banner">
    <svg class="banner-art" viewBox="0 0 1040 207" width="1040" height="207" aria-hidden="false">
      <defs>
        <linearGradient id="roomTones" x1="0" y1="0" x2="1" y2="1">
          <stop offset="0" stop-color="#cfcac4"/>
          <stop offset="0.45" stop-color="#b7a89a"/>
          <stop offset="0.75" stop-color="#6b5140"/>
          <stop offset="1" stop-color="#a89a8c"/>
        </linearGradient>
      </defs>
      <rect class="project-photo" x="600" y="0" width="440" height="207" fill="url(#roomTones)" role="img" aria-label="Photo of a finished basement wet bar with wood cabinets and lit floating shelves"/>
      <rect class="panel" x="0" y="0" width="632" height="207" fill="var(--charcoal)"/>
      <circle class="panel-curve" cx="632" cy="104" r="96" fill="var(--charcoal)"/>
      <path class="accent-arc" d="M 640 10 A 94 94 0 0 1 650 198" fill="none" stroke="var(--red)" stroke-width="9"/>
      <circle class="badge-ring" cx="632" cy="104" r="76" fill="var(--red)"/>
      <circle class="badge" cx="632" cy="104" r="66" fill="var(--white)"/>
    </svg>

    <h1 class="headline">BASEMENTS</h1>
    <p class="services">Kitchens &amp; Bathrooms</p>
    <div class="phone-strip"></div>
    <span class="phone">(612) 740-9268</span>
    <span class="website">www.tallowbrookhomes.com</span>

    <div class="brand">
      <span class="brand-mark"></span>
      <span class="brand-name">TALLOWBROOK<br>HOMES</span>
    </div>
  </div>
</body>
</html>
```